Business cards and logo for kitchen and bath remodeling company

We want an elegant card but that calls attention something unique and when people see it they remember us. A log that we can use for our own. We are a kitchen and bathroom remodeling company. We are 3 partners staring the company we are located in seattle washington usa. We try to give the best experience and luxury look in our projects and we are looking to show that in our cards. I added a sample of a card I really like. I like the black and gold look but gray blue or green in a metallic look would look nice. I'm open to any color.

Target Market(s)

Home owners.

Industry/Entity Type

Construction

Contact Information for Business Card

Larchmont and Vey builders

Colors

Designer to choose colors to be used in the design.

Requirements
Must have
• Make a Logo
• Logo to be unique
• Name of company larchmont and vey builders
Nice to have
• Have a good color scheme
• Front design to connect with back of card

```html
<!DOCTYPE html>
<html lang="en">
<head>
<meta charset="utf-8">
<title>Larchmont and Vey Builders — Business Cards</title>
<link rel="stylesheet" href="https://fonts.googleapis.com/css2?family=Open+Sans:wght@400;600&display=swap">
<style>
  :root {
    --backdrop: #1a1a1a;
    --card: #2a2928;
    --gold: #c9a34e;
    --gold-soft: #b38f3f;
  }
  * { margin: 0; padding: 0; box-sizing: border-box; }
  html, body {
    width: 1200px; height: 1021px; overflow: hidden;
    background: var(--backdrop);
    font-family: "Open Sans", Arial, sans-serif;
  }
  .stage {
    position: relative; width: 1200px; height: 1021px;
    display: flex; flex-direction: column; align-items: center; justify-content: center; gap: 70px;
  }
  .card {
    position: relative; width: 630px; height: 360px;
    background: var(--card);
    box-shadow: 0 12px 30px rgba(0,0,0,.55);
    color: var(--gold);
  }
  /* front */
  .card-front { display: flex; flex-direction: column; align-items: center; justify-content: center; }
  .brand { display: flex; align-items: center; gap: 14px; }
  .brand-square { width: 22px; height: 22px; background: var(--gold); }
  .brand-name {
    font-weight: 400; font-size: 27px; letter-spacing: 2px; text-transform: uppercase;
  }
  .brand-rule { width: 400px; height: 1px; background: var(--gold-soft); margin-top: 18px; }
  /* back */
  .card-back { padding: 120px 0 0 95px; }
  .holder-name {
    font-weight: 600; font-size: 21px; letter-spacing: 1px; text-transform: uppercase;
    margin-left: 95px;
  }
  .back-rule { width: 430px; height: 1px; background: var(--gold-soft); margin: 10px 0 8px; }
  .contact-line { display: flex; align-items: center; gap: 6px; font-size: 15px; }
  .contact-line svg { width: 14px; height: 14px; }
  .contact-gap { width: 14px; }
  .web {
    font-size: 15px; letter-spacing: 6.2px; margin-top: 4px; color: var(--gold-soft);
  }
</style>
</head>
<body>
<main class="stage">
  <section class="card card-front" aria-label="Card front">
    <div class="brand">
      <span class="brand-square"></span>
      <span class="brand-name">Larchmont and Vey builders</span>
    </div>
    <div class="brand-rule"></div>
  </section>

  <section class="card card-back" aria-label="Card back">
    <p class="holder-name">Marisol Trevane</p>
    <div class="back-rule"></div>
    <p class="contact-line">
      <svg viewBox="0 0 14 14" fill="none" stroke="currentColor" stroke-width="1.2"><rect x="3.5" y="1" width="7" height="12" rx="1"/><line x1="6" y1="11" x2="8" y2="11"/></svg>
      <span>206 5550147</span>
      <span class="contact-gap"></span>
      <svg viewBox="0 0 14 14" fill="none" stroke="currentColor" stroke-width="1.2"><rect x="1" y="3" width="12" height="8"/><polyline points="1,3 7,8 13,3"/></svg>
      <span>info@larchmontveybuilders.com</span>
    </p>
    <p class="web">www.larchmontveybuilders.com</p>
  </section>
</main>
</body>
</html>
```